The Lakeshore Classic promotional poster

The Lakeshore Classic celebrates its centennial in 2014 - a professional golf tournament benefiting Prairie Youth Links Federation. Looking for one poster to promote playing, volunteering, sponsoring and spectating.

Major fundraising initiative for junior golf.

This creative could lead to future work with flyers, promotional postcards, web design, etc.

Website with full history of event is www.thelakeshoreclassic.com

benefiting charity website www.pylf.org
Updates

Project Deadline Extended
Reason: Have been contacted by more designers looking to submit, so extended deadline. Excited about this branding opportunity for our event!

We have updated the deadline and added a new centennial logo to be incorporated. Any "Chicago" additional feel and call to action appreciated - what should people seeing the poster do? Play, volunteer, spectate, donate, sponsor....

Target Market(s)

Corporate decision-makers looking for involvement in golf opportunities for customer entertainment as well as those interested in playing and spectating opportunities. Males 28-45.

Industry/Entity Type

Charity

Requirements
Must have
• 11x17 or 12x18 design preferred

www.thelakeshoreclassic.com

Organized by and benefiting the Prairie Youth Links Federation

Marrowby Golf logo

Partial schedule of events listing:
Friday/Saturday events, Oct 5-7 Championship Rounds

http://www.thelakeshoreclassic.com/schedule.html

```html
<!DOCTYPE html>
<html lang="en">
<head>
<meta charset="utf-8">
<title>The Lakeshore Classic – Championship Poster</title>
<link rel="stylesheet" href="https://fonts.googleapis.com/css2?family=Open+Sans:ital,wdth,wght@0,75..100,400..800;1,75..100,400..800&display=swap">
<style>
  :root {
    --backdrop: #c6c6c6;
    --sky-dark: #767e89;
    --sky-light: #aeb2b8;
    --tree: #3d5526;
    --fairway: #77a33c;
    --fairway-deep: #557f26;
    --red: #d21f2d;
    --red-panel: rgba(214, 32, 44, 0.9);
    --ice: #cde6f5;
    --white: #ffffff;
    --cream: #e9e6df;
    --ink: #3a3a3a;
    --maroon: #8c1d26;
  }
  * { box-sizing: border-box; margin: 0; padding: 0; }
  html, body { width: 1200px; height: 1000px; overflow: hidden; }
  body { background: var(--backdrop); font-family: "Open Sans", Arial, sans-serif; position: relative; }

  .poster { position: absolute; left: 85px; top: 22px; width: 619px; height: 955px; overflow: hidden; }
  .poster-photo {
    position: absolute; inset: 0;
    background: linear-gradient(180deg, var(--sky-dark) 0%, var(--sky-light) 22%, var(--tree) 30%, #4f6d2f 40%, var(--fairway) 55%, var(--fairway-deep) 100%);
  }

  .title {
    position: absolute; left: 18px; top: 26px; width: 585px;
    font-size: 55px; font-weight: 700; font-stretch: 82%; color: var(--ice);
    letter-spacing: 0.5px; white-space: nowrap; text-shadow: 0 1px 3px rgba(0,0,0,.25);
  }
  .dates {
    position: absolute; left: 20px; top: 104px;
    font-size: 40px; font-weight: 800; font-stretch: 90%; color: var(--red); white-space: nowrap;
  }
  .centennial {
    position: absolute; left: 420px; top: 118px; width: 175px; height: 44px;
    background: var(--white); border-radius: 22px; border: 2px solid var(--red);
    display: flex; align-items: center; justify-content: center;
    font-size: 14px; font-weight: 700; color: var(--red); font-stretch: 85%;
  }
  .tagline {
    position: absolute; left: 22px; top: 170px;
    font-size: 18px; font-style: italic; font-weight: 600; font-stretch: 88%; color: var(--white);
    line-height: 28px; text-shadow: 0 1px 2px rgba(0,0,0,.35);
  }
  .tagline span { display: block; }
  .tagline span + span { padding-left: 79px; }

  .schedule-heading { position: absolute; left: 0; top: 293px; width: 333px; }
  .schedule-heading .kicker {
    display: block; height: 38px; padding-left: 68px;
    background: rgba(235, 235, 235, 0.82); border-radius: 0 6px 6px 0;
    font-size: 31px; font-weight: 800; font-stretch: 85%; color: var(--red); line-height: 38px;
  }
  .schedule-heading .main {
    display: block; text-align: right; padding-right: 6px; margin-top: 4px;
    font-size: 42px; font-weight: 500; font-stretch: 90%; color: var(--ice); line-height: 44px;
    text-shadow: 0 1px 3px rgba(0,0,0,.3);
  }

  .schedule {
    position: absolute; left: 349px; top: 246px; width: 248px; height: 448px;
    background: var(--red-panel); border: 1.5px solid #f3c7c9; border-radius: 8px;
    padding: 13px 6px 0; text-align: center; color: var(--white);
  }
  .day { margin-bottom: 11px; }
  .day h3 { font-size: 15.5px; font-weight: 700; font-stretch: 90%; margin-bottom: 3px; }
  .day li { list-style: none; font-size: 8.6px; font-style: italic; font-weight: 600; font-stretch: 85%; line-height: 17px; }

  .partners {
    position: absolute; left: 351px; top: 718px; width: 268px; height: 177px;
    background: var(--cream); border-top-left-radius: 190px 60px;
    text-align: center; color: var(--ink);
  }
  .partner-host { position: absolute; left: 0; top: 26px; width: 268px; }
  .partner-name { font-size: 15px; font-weight: 600; color: var(--maroon); font-stretch: 88%; }
  .partner-note { font-size: 9.5px; font-style: italic; font-weight: 700; font-stretch: 85%; line-height: 14px; margin-top: 6px; }
  .partners hr { position: absolute; left: 45px; top: 94px; width: 210px; border: 0; border-top: 1px solid var(--maroon); }
  .partner-charity { position: absolute; left: 26px; top: 112px; width: 236px; display: flex; align-items: center; gap: 10px; text-align: left; }
  .charity-name { font-size: 22px; font-weight: 700; color: var(--ink); letter-spacing: 1px; }
  .partner-charity .partner-note { margin-top: 0; }

  .footer {
    position: absolute; left: 0; bottom: 0; width: 619px; height: 60px;
    background: var(--red); display: flex; align-items: center; justify-content: center;
    font-size: 30px; font-weight: 700; font-stretch: 85%; color: var(--ice); letter-spacing: 1.2px;
  }
</style>
</head>
<body>
  <main class="poster">
    <div class="poster-photo" role="img" aria-label="Photograph of a golfer in a blue shirt kissing the championship trophy on a tree-lined course under a cloudy sky"></div>

    <h1 class="title">THE LAKESHORE CLASSIC</h1>
    <p class="dates">OCTOBER 3-7, 2014</p>
    <div class="centennial">The Lakeshore Classic</div>
    <p class="tagline"><span>Where 100 Years of Golf History ...</span><span>Meet Golf History in the Making</span></p>

    <h2 class="schedule-heading"><span class="kicker">CHAMPIONSHIP</span><span class="main">SCHEDULE<br>OF EVENTS</span></h2>

    <section class="schedule">
      <div class="day"><h3>FRIDAY, OCTOBER 3</h3><ul>
        <li>• The Lakeshore Classic Friends &amp; Family Pro-Am – Morning</li>
        <li>• The Lakeshore Classic Pro-Am • Afternoon</li></ul></div>
      <div class="day"><h3>SATURDAY, OCTOBER 4</h3><ul>
        <li>• Practice Rounds – Afternoon</li>
        <li>• The Lakeshore Classic Expo Area – All Day</li>
        <li>• Junior Walking Clinic – 1 p.m. - 4 p.m.</li></ul></div>
      <div class="day"><h3>SUNDAY, OCTOBER 5</h3><ul>
        <li>• The Lakeshore Classic, First Rounds, 1st and 10th tees</li>
        <li>8 a.m. - 2 p.m.</li>
        <li>• The Lakeshore Classic Junior Pro-Am – 1 p.m.</li></ul></div>
      <div class="day"><h3>MONDAY, OCTOBER 6</h3><ul>
        <li>• The Lakeshore Classic, Second Round, 1st and 10th tees</li>
        <li>8 a.m. - 2 p.m.</li>
        <li>• The Lakeshore Classic Expo Area – All Day</li></ul></div>
      <div class="day"><h3>TUESDAY, OCTOBER 7</h3><ul>
        <li>• The Lakeshore Classic, Championship Round, 1st tee</li>
        <li>8 a.m. - 12 p.m.</li>
        <li>• The Lakeshore Classic Expo Area – closes at 12 noon</li>
        <li>• Trophy Presentation – upon conclusion of play</li></ul></div>
    </section>

    <aside class="partners">
      <div class="partner-host">
        <p class="partner-name">Marrowby Golf</p>
        <p class="partner-note">Marrowby Golf will serve as the<br>host site of The Lakeshore Classic.</p>
      </div>
      <hr>
      <div class="partner-charity">
        <span class="charity-name">PYLF</span>
        <p class="partner-note">Proceeds from The Lakeshore Classic benefit The Prairie Youth Links Federation (PYLF.)</p>
      </div>
    </aside>

    <footer class="footer">WWW.THELAKESHORECLASSIC.COM</footer>
  </main>
</body>
</html>
```